Web Concept Design - modernize website

Looking to modernize our current website. http :// hvmcoldbrook . com

Color Scheme: Use uploaded palette. (Black, Silver, Dark Purple, Greyish Blue)

The website needs to have a patient-friendly, community-friendly feel to it. While still being a professional medical website. We don't want it to have a cold, clinical feel.

Information on home page needs to be split into their own separate pages with designs for each.

Home Page:
Harborview Walk-In & Family Care is a family practice and urgent care clinic dedicated to providing high quality, compassionate health care, to patients of all ages.
Hours of operation:
Monday-Friday 9am-6:30pm
Saturday: CLOSED
Sunday: CLOSED
Primary Care visits will be by appointment only.
We will accept our last new patient at 6:00p and our last established patient at 6:30p.
We will no longer be doing DOT Physicals.

At bottom of home page:

Harborview Walk-In & Family Care understands that information about your health is private and we know how important it is to keep your medical information protected. We follow all HIPAA guidelines to protect the privacy of your medical records. The privacy act below explains our privacy practices and how we may use and disclose your medical information. If you would like for Harborview Walk-In & Family Care to release any or all of your medical information to others, you can make the request by signing a release and bring it with you at your next visit. If you would like to contact someone about the privacy and/or use of your medical information, you may contact us at 205-381-7260.

Click here for HIPAA document.

Click here for Medical Release form.

---------------

Services Page:
We provide family and urgent care for patients of all ages.

-Annual physicals
-Pre-employment drug screening
-Women's care including pap smears
-Screening and treatment for diabetes, hypertension and cholesterol
-All minor trauma such as abscesses, lacerations, burns and fractures
-Minor skin complaints
-Onsite LAB/XRAY/EKG
-Weight loss
-Adult and Pediatric Vaccinations
-Osteopathic manual medicine
-Medical pain management

-----

Payment & Insurance Page:
We now have online bill pay for patient balances. Please visit https://secure.paytrellixmed.example/hvmc382pay to pay your bill today!

We currently accept all forms of insurance with the exception of Medicaid. Please bring a copy of your insurance card and photo ID upon visit. We are also a Servimed prime provider. We do accept self-pay for patients who do not have insurance.

----

Meet Our Providers Page:

Dr. Daniel (Dan) Whitcomb, DO
Family Practice Physician

Professional Experience
April 4, 2010 to Present Harborview Walk-In & Family Care Owner
12 years of Emergency Medicine experience
6/1994 - 7/1997 KLT Birmingham, AL
Family Medicine Residency
10/1997 to Present Board Certified in Family Medicine
Recertified 2004
Education
9/1990 to 5/1994 Eastbrook College of Osteopathic Medicine
Old Westbury, New York
Degree: Doctor of Osteopathic Medicine
9/1985 to 5/1989 Caldwell-Ridgemont College
Birmingham, Alabama
Degree: Bachelor of Science
Membership
National Guild of Family Practitioners
Physicians Council of the State of Alabama

----

Navigation Bar should have links for all the above pages + NEW PATIENTS + Access Your Medical Records (feel free to be creative with how you design this). We don't want the navigation bar to be too crowded.

Target Market(s)

Medical Patients

Number of Pages Required

5+ page

Colors

Designer to choose colors to be used in the design.

Requirements
Must have
• Designs for all pages
• Keep it professional
Nice to have
• Be creative!
Should not have
• No cold clinical, medical websites

```html
<!DOCTYPE html>
<html lang="en">
<head>
<meta charset="utf-8">
<title>New Patients – Harborview Walk-In &amp; Family Care</title>
<link href="https://fonts.googleapis.com/css2?family=Josefin+Sans:wght@600;700&family=Ubuntu:wght@400;500&display=swap" rel="stylesheet">
<style>
  :root {
    --purple: #5c2079;
    --purple-deep: #4b1866;
    --ink: #333333;
    --body-ink: #3a3a3a;
    --white: #ffffff;
    --map-tone: #e6e4e0;
    --wood-tone: #c9a57a;
    --paper-tone: #eeeeec;
    --store-tone: #8d8f94;
  }
  * { box-sizing: border-box; margin: 0; padding: 0; }
  html, body { width: 893px; height: 1200px; overflow: hidden; background: var(--white); }
  body { position: relative; font-family: "Ubuntu", sans-serif; color: var(--body-ink); }
  .abs { position: absolute; }

  .contact-row { display: flex; align-items: center; font-family: "Josefin Sans", sans-serif; font-weight: 700; font-size: 8.5px; color: var(--purple); white-space: nowrap; }
  .contact-item { display: flex; align-items: center; gap: 9px; }
  .contact-item svg { flex: none; }
  .social { display: flex; gap: 11px; }
  .social span { width: 20px; height: 20px; border: 1.5px solid currentColor; border-radius: 50%; display: block; }

  .top-bar { left: 14px; top: 0; width: 866px; height: 26px; justify-content: space-between; }

  .site-header { left: 0; top: 26px; width: 893px; height: 62px; background: var(--purple); }
  .brand { position: absolute; left: 13px; top: 8px; font-family: "Josefin Sans", sans-serif; font-weight: 700; font-size: 21px; line-height: 27px; letter-spacing: 1px; color: var(--white); text-transform: uppercase; }
  .main-nav { position: absolute; right: 13px; top: 24px; display: flex; gap: 32px; font-family: "Josefin Sans", sans-serif; font-weight: 700; font-size: 11.5px; letter-spacing: .5px; color: var(--white); }

  .sub-bar { left: 0; top: 88px; width: 893px; height: 62px; border-bottom: 1.5px solid var(--purple); }
  .hours { position: absolute; left: 14px; top: 8px; font-family: "Josefin Sans", sans-serif; font-weight: 700; font-size: 15px; line-height: 27px; color: var(--purple); }
  .sub-nav { position: absolute; right: 14px; top: 24px; display: flex; gap: 32px; font-family: "Josefin Sans", sans-serif; font-weight: 700; font-size: 11px; letter-spacing: .6px; color: var(--purple); }
  .sub-shadow { left: 0; top: 151px; width: 893px; height: 22px; background: linear-gradient(#ececec, rgba(255,255,255,0)); }

  .page-title { left: 0; top: 192px; width: 893px; text-align: center; font-family: "Josefin Sans", sans-serif; font-weight: 700; font-size: 36px; letter-spacing: 2px; color: var(--ink); }

  .intro { left: 14px; top: 262px; width: 444px; font-size: 17px; line-height: 19.4px; letter-spacing: .6px; color: var(--body-ink); }
  .intro-photo { left: 469px; top: 265px; width: 410px; height: 273px; background: linear-gradient(160deg, var(--wood-tone) 0%, var(--wood-tone) 30%, var(--paper-tone) 55%, #d9d6d0 100%); }
  .download-lead { left: 13px; top: 494px; width: 440px; font-size: 19px; line-height: 22px; letter-spacing: .6px; color: #222; }

  .form-buttons { left: 12px; top: 554px; width: 869px; height: 137px; display: flex; gap: 7.6px; }
  .form-button { flex: 1; background: var(--purple); color: var(--white); display: flex; align-items: center; justify-content: center; text-align: center; font-size: 21px; line-height: 24px; letter-spacing: 1px; }

  .map { left: 14px; top: 707px; width: 566px; height: 325px; background: var(--map-tone); }
  .storefront { left: 596px; top: 707px; width: 285px; height: 326px; border: 1px solid #333; background: linear-gradient(#c9ccd1 0%, #b5b8bd 30%, #3a3b3e 36%, var(--store-tone) 60%, #6f7176 100%); }

  .site-footer { left: 0; top: 1066px; width: 893px; height: 134px; background: var(--purple); color: var(--white); }
  .footer-about { position: absolute; left: 14px; top: 13px; width: 440px; font-size: 13px; line-height: 14.5px; letter-spacing: .4px; }
  .footer-brand { position: absolute; right: 12px; top: 12px; text-align: right; font-family: "Josefin Sans", sans-serif; font-weight: 700; font-size: 21px; line-height: 27px; letter-spacing: 1px; text-transform: uppercase; }
  .footer-contact { position: absolute; left: 14px; top: 72px; width: 866px; justify-content: space-between; color: var(--white); }
  .copyright { position: absolute; left: 0; top: 112px; width: 893px; text-align: center; font-size: 13px; letter-spacing: .6px; }
</style>
</head>
<body>

<div class="abs contact-row top-bar">
  <div class="contact-item">
    <svg width="22" height="20" viewBox="0 0 24 24" fill="currentColor"><path d="M6.6 2.5l3 3.4-1.9 2.3c1.3 2.8 3.4 5 6.2 6.3l2.3-1.9 3.4 3-2 3.6C10.2 18.6 4.7 12.8 3 5.1z"/></svg>
    <span>205.381.7260</span>
  </div>
  <div class="contact-item">
    <svg width="24" height="22" viewBox="0 0 24 22" fill="currentColor"><rect x="6" y="1" width="12" height="6"/><rect x="1" y="8" width="22" height="9" rx="2"/><rect x="6" y="14" width="12" height="7" fill="#fff" stroke="currentColor" stroke-width="2"/></svg>
    <span>205.381.7295</span>
  </div>
  <div class="contact-item">
    <svg width="30" height="20" viewBox="0 0 30 20" fill="none" stroke="currentColor" stroke-width="2.2"><rect x="1.5" y="1.5" width="27" height="17"/><path d="M1.5 1.5l13.5 10 13.5-10M1.5 18.5l10-9M28.5 18.5l-10-9"/></svg>
    <span>hvwalkin@mailhub.example</span>
  </div>
  <div class="contact-item">
    <svg width="16" height="22" viewBox="0 0 16 22" fill="currentColor"><path d="M8 0a8 8 0 0 0-8 8c0 6 8 14 8 14s8-8 8-14a8 8 0 0 0-8-8zm0 11a3 3 0 1 1 0-6 3 3 0 0 1 0 6z"/></svg>
    <span>2718 Alder Creek Road Suite 204 &nbsp;Coldbrook, AL 35190</span>
  </div>
  <div class="social"><span></span><span></span><span></span></div>
</div>

<header class="abs site-header">
  <div class="brand">Harborview Walk-In<br>&amp; Family Care</div>
  <nav class="main-nav"><span>HOME</span><span>SERVICES</span><span>PAYMENT &amp; INSURANCE</span><span>OUR PROVIDERS</span></nav>
</header>

<div class="abs sub-bar">
  <div class="hours">Monday - Friday: 9am - 6:30pm<br>Saturday, Sunday: CLOSED</div>
  <nav class="sub-nav"><span>NEW PATIENTS</span><span>ACCESS YOUR MEDICAL RECORDS</span></nav>
</div>
<div class="abs sub-shadow"></div>

<h1 class="abs page-title">NEW PATIENTS</h1>

<p class="abs intro">Lorem ipsum dolor sit amet, consectetur adipiscing elit. Aenean vel ultrices ipsum, a aliquam sem. Sed viverra cursus placerat. Nulla neque dui, malesuada ut fringilla et, euismod nec mi. Mauris aliquam congue urna at convallis. Pellentesque faucibus efficitur lacus, sed eleifend orci aliquam in. Aliquam fringilla, orci non ultricies malesuada, sem est pulvinar nisi, at sollicitudin libero erat sit amet orci. Etiam finibus id enim pulvinar volutpat. Vestibulum luctus aliquam risus id rhoncus.</p>

<div class="abs intro-photo" role="img" aria-label="Photo of a hand signing a paper form with a pen on a wooden desk"></div>

<p class="abs download-lead">Click Below to Download New Patient Forms and Handbook:</p>

<div class="abs form-buttons">
  <div class="form-button">New Adult<br>Patient Forms</div>
  <div class="form-button">New Pediatric<br>Patient Forms</div>
  <div class="form-button">Medical Records<br>Release Form</div>
  <div class="form-button">New Patient<br>Handbook</div>
</div>

<div class="abs map" role="img" aria-label="Map showing the clinic location at 2718 Alder Creek Rd"></div>
<div class="abs storefront" role="img" aria-label="Photo of the clinic storefront with its sign above the glass entrance"></div>

<footer class="abs site-footer">
  <p class="footer-about">Harborview Walk-In &amp; Family Care is a family practice and urgent care clinic dedicated to providing high quality, compassionate health care, to patients of all ages.</p>
  <div class="footer-brand">Harborview Walk-In<br>&amp; Family Care</div>
  <div class="contact-row footer-contact">
    <div class="contact-item">
      <svg width="22" height="20" viewBox="0 0 24 24" fill="currentColor"><path d="M6.6 2.5l3 3.4-1.9 2.3c1.3 2.8 3.4 5 6.2 6.3l2.3-1.9 3.4 3-2 3.6C10.2 18.6 4.7 12.8 3 5.1z"/></svg>
      <span>205.381.7260</span>
    </div>
    <div class="contact-item">
      <svg width="24" height="22" viewBox="0 0 24 22" fill="currentColor"><rect x="6" y="1" width="12" height="6"/><rect x="1" y="8" width="22" height="9" rx="2"/><rect x="6" y="14" width="12" height="7" fill="#5c2079" stroke="currentColor" stroke-width="2"/></svg>
      <span>205.381.7295</span>
    </div>
    <div class="contact-item">
      <svg width="30" height="20" viewBox="0 0 30 20" fill="none" stroke="currentColor" stroke-width="2.2"><rect x="1.5" y="1.5" width="27" height="17"/><path d="M1.5 1.5l13.5 10 13.5-10M1.5 18.5l10-9M28.5 18.5l-10-9"/></svg>
      <span>hvwalkin@mailhub.example</span>
    </div>
    <div class="contact-item">
      <svg width="16" height="22" viewBox="0 0 16 22" fill="currentColor"><path d="M8 0a8 8 0 0 0-8 8c0 6 8 14 8 14s8-8 8-14a8 8 0 0 0-8-8zm0 11a3 3 0 1 1 0-6 3 3 0 0 1 0 6z"/></svg>
      <span>2718 Alder Creek Road Suite 204 &nbsp;Coldbrook, AL 35190</span>
    </div>
    <div class="social"><span></span><span></span><span></span></div>
  </div>
  <p class="copyright">All rights reserved © 2018. Harborview Walk-In &amp; Family Care</p>
</footer>

</body>
</html>
```